Emergency Management Consulting Flyer

Company name: Stone Harbor Emergency Management

I am looking for a postcard design for my emergency management consulting business. I'm looking for something that has some colors and is double sided, on side with the information on services provided and the other side with the contact information. For the main side I'm looking for the following:

How prepared are you?

Services Provided:
Healthcare Preparedness
EOC Support
Emergency Planning
Mitigation Planning
Business Continuity
Disaster Response
Training and Exercises
Project Management
And more

Affordable for small and large organizations
Stand-by contracts available

On the back side, I'm looking for Contact Us section.

Overall I'm looking for something a bit more modern and need to have at least one disaster photo. If you have questions please message me.

Target Market(s)

Government, Healthcare Facilities, Businesses

Industry/Entity Type

Consulting

Requirements
Must have
• Disaster Picture, modern looking
• For the main side I'm looking for the following:
• How prepared are you?
• Services Provided:
• Healthcare Preparedness
• EOC Support
• Emergency Planning
• Mitigation Planning
• Business Continuity
• Disaster Response
• Training and Exercises
• Project Management
• And more
• Affordable for small and large organizations
• Stand-by contracts available

```html
<!DOCTYPE html>
<html lang="en">
<head>
<meta charset="utf-8">
<title>Stone Harbor Emergency Management – Postcard</title>
<link rel="stylesheet" href="https://fonts.googleapis.com/css2?family=Questrial&family=Noto+Serif&family=Oswald:wght@500&family=Open+Sans:ital,wght@0,300;0,700;1,700&family=Roboto+Condensed:ital,wght@0,700;1,700&family=Arimo&display=swap">
<style>
  :root{
    --backdrop:#4d2c0d;
    --storm-dark:#4a545c;
    --storm-light:#9aa3a6;
    --field:#3c4a33;
    --yellow:#f4d31c;
    --gold:#f2b51e;
    --bullet:#f59a1c;
    --orange:#f28a25;
    --red:#e8412f;
    --white:#ffffff;
    --ink:#3a3a3c;
    --blue-top:#1d72c0;
    --blue-bottom:#223f8e;
    --mail-grey:#e6e7e8;
  }
  *{box-sizing:border-box;margin:0;padding:0}
  html,body{width:801px;height:1200px;overflow:hidden;background:var(--backdrop)}
  .canvas{position:relative;width:801px;height:1200px}
  .card{position:absolute;box-shadow:4px 6px 10px rgba(0,0,0,.55);overflow:hidden}

  /* front */
  .front{left:42px;top:44px;width:712px;height:550px}
  .storm-photo{position:absolute;inset:0;
    background:
      radial-gradient(ellipse 45% 60% at 72% 45%, rgba(40,42,48,.85) 0 40%, transparent 70%),
      linear-gradient(180deg,var(--storm-dark) 0%,var(--storm-light) 55%,#7c8a80 72%,var(--field) 100%)}
  .headline{position:absolute;left:30px;top:30px;font-family:"Questrial",sans-serif;
    font-size:56px;line-height:68px;color:var(--yellow);letter-spacing:1px}
  .services-title{position:absolute;left:32px;top:207px;font-family:"Questrial",sans-serif;
    font-size:22px;color:var(--gold);letter-spacing:.5px}
  .services{position:absolute;left:32px;top:249px;list-style:none}
  .services li{position:relative;padding-left:32px;height:30.6px;font-family:"Noto Serif",serif;
    font-size:19px;line-height:30px;color:#f2f2f2;text-shadow:0 1px 2px rgba(0,0,0,.4)}
  .services li::before{content:"";position:absolute;left:0;top:7px;width:17px;height:17px;border-radius:50%;
    background:radial-gradient(circle at 45% 40%,#ffe27a 0 25%,var(--bullet) 60%,#c9650d 100%);
    box-shadow:0 0 0 2px rgba(255,255,255,.35)}
  .offer{position:absolute;left:358px;top:338px;width:314px;height:96px;border-radius:4px;
    background:linear-gradient(90deg,var(--orange),var(--red));
    font-family:"Oswald",sans-serif;font-weight:500;font-size:22px;line-height:26.5px;
    color:var(--white);text-align:center;padding-top:8px;text-shadow:0 1px 2px rgba(0,0,0,.35)}
  .brand-plate{position:absolute;left:358px;top:442px;width:314px;height:82px;border-radius:4px;
    background:var(--white);display:flex;align-items:center;padding-left:14px;gap:12px}
  .brand-dot{width:44px;height:44px;border-radius:50%;background:var(--blue-top);flex:none}
  .brand-name{font-family:"Questrial",sans-serif;font-size:19px;line-height:22px;color:var(--ink)}

  /* back */
  .back{left:42px;top:614px;width:711px;height:550px;background:var(--white)}
  .domino-photo{position:absolute;left:0;top:0;width:294px;height:178px;
    clip-path:polygon(0 0,60px 0,294px 178px,0 178px);
    background:linear-gradient(120deg,#2b2b2e 0%,#6e6a66 30%,#d9b78f 55%,#f1e6d6 80%)}
  .back-brand{position:absolute;left:184px;top:30px;display:flex;align-items:center;gap:14px}
  .back-brand .brand-dot{width:56px;height:56px}
  .back-brand .brand-name{font-size:25px;line-height:28px}
  .mail-zones{position:absolute;left:0;top:0}
  .zone-label{position:absolute;font-family:"Arimo",sans-serif;font-size:19px;line-height:25px;
    color:#111;text-align:center;transform:translateX(-50%)}
  .contact{position:absolute;left:28px;top:196px;width:303px;height:248px;
    background:linear-gradient(180deg,var(--blue-top),var(--blue-bottom));color:var(--white);text-align:center}
  .contact-head{height:34px;background:linear-gradient(180deg,#f7a13a,var(--orange));
    font-family:"Open Sans",sans-serif;font-weight:700;font-size:14.5px;line-height:34px;
    text-shadow:0 1px 2px rgba(0,0,0,.35)}
  .contact-pitch{font-family:"Open Sans",sans-serif;font-weight:300;font-size:21px;line-height:30px;margin-top:9px}
  .contact-phone{font-family:"Roboto Condensed",sans-serif;font-weight:700;font-size:36px;line-height:40px;margin-top:16px}
  .contact-address{font-family:"Roboto Condensed",sans-serif;font-style:italic;font-weight:700;font-size:17px;line-height:22px;margin-top:4px}
</style>
</head>
<body>
<div class="canvas">

  <section class="card front">
    <div class="storm-photo" role="img" aria-label="Stormy sky with lightning over a grass field, businessman in a suit holding a black umbrella seen from behind"></div>
    <h1 class="headline">How prepared<br>are you?</h1>
    <h2 class="services-title">SERVICES PROVIDED:</h2>
    <ul class="services">
      <li>Healthcare Preparedness</li>
      <li>EOC Support</li>
      <li>Emergency Planning</li>
      <li>Mitigation Planning</li>
      <li>Business Continuity</li>
      <li>Disaster Response</li>
      <li>Training and Exercises</li>
      <li>Project Management</li>
      <li>And more</li>
    </ul>
    <p class="offer">Affordable for small<br>and large organizations<br>Stand-by contracts available</p>
    <div class="brand-plate">
      <span class="brand-dot"></span>
      <span class="brand-name">Stone Harbor<br>Emergency Management</span>
    </div>
  </section>

  <section class="card back">
    <div class="domino-photo" role="img" aria-label="Hand stopping a row of falling wooden dominoes"></div>
    <div class="back-brand">
      <span class="brand-dot"></span>
      <span class="brand-name">Stone Harbor<br>Emergency Management</span>
    </div>
    <svg class="mail-zones" width="711" height="550" aria-hidden="true">
      <polygon fill="#e6e7e8" points="534,17 692,17 692,532 90,532 90,454 344,454 344,176 534,176"/>
    </svg>
    <span class="zone-label" style="left:615px;top:71px">Postage<br>Area</span>
    <span class="zone-label" style="left:520px;top:216px">Address Area</span>
    <span class="zone-label" style="left:399px;top:484px">Barcode Area</span>
    <div class="contact">
      <div class="contact-head">Stone Harbor Emergency Management</div>
      <p class="contact-pitch">Affordable for small<br>and large organizations<br>Stand-by contracts available</p>
      <p class="contact-phone">Call: 01234 56789</p>
      <p class="contact-address">Suite 00, Cityname, Countyname</p>
    </div>
  </section>

</div>
</body>
</html>
```